Surface Protection company needs cards

We are a New Zealand company that will apply nanotechnology coatings on surfaces to prevent growth and spread of bacteria, viruses, mold etc with a sprayer. We deal with large corporates, airlines, hospitals and schools so we are after a new modern, simple and clean look that will have great visual impact.
We a company that is focused on prevention and protection.

Company name, Vela Shield

Subtext, Antimicrobial Surface Protection

Logo, VS

Target Market(s)

Hospitals, Transport agencies, Airlines, Corporate entities

Contact Information for Business Card

Company name, VelaShield
Logo, VS

Gareth Tolley
velashieldnz@postbox.example
+64219305562
www.velashield.example.nz

Requirements
Must have
• Simple clean look.
Nice to have
• We apply nano coatings so try and incorporate this into a theme somehow

```html
<!DOCTYPE html>
<html lang="en">
<head>
<meta charset="utf-8">
<title>Vela Shield – Business Card</title>
<link href="https://fonts.googleapis.com/css2?family=Rubik:wght@500;700&family=Lato:wght@400;700&display=swap" rel="stylesheet">
<style>
  :root {
    --backdrop: #3a3d42;
    --card-white: #ffffff;
    --card-shade: #ececec;
    --brand-blue: #1166c8;
    --brand-blue-deep: #0b4f9e;
    --brand-green: #8cc43f;
    --text-grey: #4a4a4a;
    --text-light: #e8ecf1;
  }
  * { box-sizing: border-box; margin: 0; padding: 0; }
  html, body {
    width: 1200px; height: 900px; overflow: hidden;
    background: var(--backdrop);
  }
  .sheet {
    width: 1200px; height: 900px;
    display: flex; flex-direction: column; align-items: center; justify-content: center;
    gap: 40px;
  }
  .card {
    width: 700px; height: 400px;
    border-radius: 4px;
    box-shadow: 0 12px 30px rgba(0,0,0,.45);
    position: relative; overflow: hidden;
  }
  /* Front */
  .card-front {
    background: radial-gradient(circle at 70% 60%, var(--card-white) 40%, var(--card-shade) 100%);
    padding: 48px 56px;
    font-family: "Lato", sans-serif;
    color: var(--text-grey);
  }
  .brand { display: flex; flex-direction: column; }
  .brand-name {
    font-family: "Rubik", sans-serif; font-weight: 700;
    font-size: 46px; line-height: 1; color: var(--brand-blue);
    letter-spacing: -0.5px;
  }
  .brand-tagline {
    font-size: 12.5px; letter-spacing: 1.2px; text-transform: uppercase;
    color: var(--text-grey); margin-top: 6px;
  }
  .person { margin-top: 40px; }
  .person-name {
    font-family: "Rubik", sans-serif; font-weight: 700;
    font-size: 28px; color: var(--brand-blue);
  }
  .person-role { font-size: 16px; margin-top: 2px; }
  .divider {
    width: 44px; height: 3px; background: var(--brand-green);
    margin: 18px 0 16px;
  }
  .contact-list { list-style: none; font-size: 17px; line-height: 1.6; }
  .contact-list li { display: flex; align-items: center; gap: 12px; }
  .contact-icon { width: 15px; height: 15px; flex: none; }

  /* Back */
  .card-back {
    background: linear-gradient(135deg, var(--brand-blue) 0%, var(--brand-blue-deep) 100%);
    display: flex; flex-direction: column; align-items: center; justify-content: center;
    font-family: "Lato", sans-serif;
  }
  .card-back .brand-name { font-size: 72px; color: var(--text-light); }
  .card-back .brand-tagline {
    color: var(--text-light); font-size: 17px; letter-spacing: 2px; margin-top: 12px;
  }
</style>
</head>
<body>
<main class="sheet">
  <section class="card card-front">
    <div class="brand">
      <span class="brand-name">Vela Shield</span>
      <span class="brand-tagline">Antimicrobial Surface Protection</span>
    </div>
    <div class="person">
      <p class="person-name">Gareth Tolley</p>
      <p class="person-role">Director</p>
    </div>
    <div class="divider"></div>
    <ul class="contact-list">
      <li>
        <svg class="contact-icon" viewBox="0 0 16 16" aria-hidden="true">
          <path d="M4 1.5 L6 4.5 L4.8 6.2 C5.6 8 7.9 10.4 9.8 11.2 L11.5 10 L14.5 12 L13 14.5 C7.5 14 2 8.5 1.5 3 Z" fill="var(--brand-blue)"/>
        </svg>
        +64219305562
      </li>
      <li>
        <svg class="contact-icon" viewBox="0 0 16 16" aria-hidden="true">
          <rect x="1.5" y="3.5" width="13" height="9" fill="none" stroke="var(--brand-blue)" stroke-width="1.5"/>
          <path d="M1.5 3.5 L8 9 L14.5 3.5" fill="none" stroke="var(--brand-blue)" stroke-width="1.5"/>
        </svg>
        velashieldnz@postbox.example
      </li>
      <li>
        <svg class="contact-icon" viewBox="0 0 16 16" aria-hidden="true">
          <circle cx="8" cy="8" r="6.5" fill="none" stroke="var(--brand-blue)" stroke-width="1.5"/>
          <ellipse cx="8" cy="8" rx="3" ry="6.5" fill="none" stroke="var(--brand-blue)" stroke-width="1.2"/>
          <path d="M1.5 8 H14.5" stroke="var(--brand-blue)" stroke-width="1.2"/>
        </svg>
        www.velashield.example.nz
      </li>
    </ul>
  </section>

  <section class="card card-back">
    <span class="brand-name">Vela Shield</span>
    <span class="brand-tagline">Antimicrobial Surface Protection</span>
  </section>
</main>
</body>
</html>
```